New Business Card Design Project

We want a modern business card that catches the attention of other remodeling companies as well as homeowners. We would like it to be informative but still simple.

Target Market(s)

Residential and other Business's

Contact Information for Business Card

TrellBrix
Phone number is 5153927048
Address is
4817 SW 3rd Lane
Marlow Bend, Iowa 50827
email is trellbrixco@quamlet.com

Requirements
Must have
• Our tagline
• Trusted | Dependable | Reasonable

```html
<!DOCTYPE html>
<html lang="en">
<head>
<meta charset="utf-8">
<title>TrellBrix Business Card</title>
<link rel="stylesheet" href="https://fonts.googleapis.com/css2?family=Montserrat:wght@800&family=Oswald:wght@500&family=Questrial&family=Roboto:wght@400;700&display=swap">
<style>
  :root {
    --backdrop: #3a3a3a;
    --card-dark: #1a1a1a;
    --card-light: #ffffff;
    --brand-blue: #0b66c8;
    --brand-orange: #d45400;
    --ink: #1b1b1b;
  }
  * { margin: 0; padding: 0; box-sizing: border-box; }
  html, body { width: 1200px; height: 1200px; overflow: hidden; }
  body { background: var(--backdrop); position: relative; }

  .card {
    position: absolute;
    left: 280px;
    width: 640px;
    height: 366px;
    overflow: hidden;
  }
  .card--front { top: 176px; background: var(--card-dark); }
  .card--back { top: 637px; background: var(--card-light); }

  .front-brand {
    position: absolute;
    left: 0; right: 0; top: 142px;
    text-align: center;
  }
  .wordmark {
    font-family: "Montserrat", sans-serif;
    font-weight: 800;
    letter-spacing: 1px;
    line-height: 1;
    white-space: nowrap;
  }
  .front-brand .wordmark { font-size: 52px; color: var(--brand-blue); }
  .tagline {
    margin-top: 12px;
    font-family: "Oswald", sans-serif;
    font-weight: 500;
    font-size: 21px;
    color: var(--brand-blue);
    letter-spacing: 0.3px;
    white-space: nowrap;
  }

  .contact-list {
    position: absolute;
    left: 44px; top: 78px;
    list-style: none;
    font-family: "Questrial", sans-serif;
    font-size: 23px;
    color: var(--ink);
    line-height: 28px;
    white-space: nowrap;
  }
  .contact-item { display: flex; align-items: flex-start; margin-bottom: 8px; }
  .contact-item .icon { width: 22px; height: 22px; margin: 3px 14px 0 0; flex: none; }
  .contact-item--email { margin-top: 4px; }

  .person {
    position: absolute;
    right: 42px; top: 60px;
    text-align: right;
    font-family: "Roboto", sans-serif;
    color: var(--ink);
    white-space: nowrap;
  }
  .person-name { font-weight: 700; font-size: 30px; line-height: 34px; }
  .person-role { font-weight: 400; font-size: 21px; line-height: 24px; }

  .wave { position: absolute; left: 0; top: 0; width: 640px; height: 366px; }

  .card--back .wordmark {
    position: absolute;
    right: 42px; top: 292px;
    font-size: 41px;
    color: var(--card-light);
  }
</style>
</head>
<body>
  <section class="card card--front" aria-label="Card front">
    <div class="front-brand">
      <div class="wordmark">TRELLBRIX</div>
      <div class="tagline">TRUSTED | DEPENDABLE | REASONABLE</div>
    </div>
  </section>

  <section class="card card--back" aria-label="Card back">
    <svg class="wave" viewBox="0 0 739 421" preserveAspectRatio="none" aria-hidden="true">
      <path fill="var(--brand-orange)" d="M0,271 C110,350 260,372 372,308 C270,366 120,374 0,330 Z"/>
      <path fill="var(--brand-blue)" d="M0,346 C130,402 290,392 378,306 C440,270 505,262 565,285 C640,315 700,312 739,230 L739,421 L0,421 Z"/>
    </svg>

    <ul class="contact-list">
      <li class="contact-item">
        <svg class="icon" viewBox="0 0 24 24" aria-hidden="true"><path fill="var(--brand-blue)" d="M12 1C7.6 1 4.5 4.3 4.5 8.4 4.5 14 12 23 12 23s7.5-9 7.5-14.6C19.5 4.3 16.4 1 12 1zm0 10.4a3 3 0 1 1 0-6 3 3 0 0 1 0 6z"/></svg>
        <span>4817 SW 3rd Lane<br>Marlow Bend, Iowa 50827</span>
      </li>
      <li class="contact-item">
        <svg class="icon" viewBox="0 0 24 24" aria-hidden="true"><path fill="var(--brand-blue)" d="M6.6 10.8a15.1 15.1 0 0 0 6.6 6.6l2.2-2.2c.3-.3.7-.4 1-.2 1.1.4 2.3.6 3.6.6.6 0 1 .4 1 1V20c0 .6-.4 1-1 1C10.6 21 3 13.4 3 4c0-.6.4-1 1-1h3.5c.6 0 1 .4 1 1 0 1.3.2 2.5.6 3.6.1.3 0 .7-.2 1l-2.3 2.2z"/></svg>
        <span>5153927048</span>
      </li>
      <li class="contact-item contact-item--email">
        <svg class="icon" viewBox="0 0 24 24" aria-hidden="true"><path fill="var(--brand-blue)" d="M2 9l10-6 10 6v11H2V9zm2 1.2V18h16v-7.8l-8 5-8-5zM6 9l6 3.8L18 9l-6-3.6L6 9z"/></svg>
        <span>trellbrixco@quamlet.com</span>
      </li>
    </ul>

    <div class="person">
      <div class="person-name">DANA KESSLER</div>
      <div class="person-role">Owner</div>
    </div>

    <div class="wordmark">TRELLBRIX</div>
  </section>
</body>
</html>
```